Business Flyer

I want an updated flyer that will have the same content as the one attached but in a different format. They flyers will be passed out to the community and local businesses.

```html
<!DOCTYPE html>
<html lang="en">
<head>
<meta charset="utf-8">
<title>Twirl Juice House Flyer</title>
<link rel="stylesheet" href="https://fonts.googleapis.com/css2?family=Archivo+Black&family=Roboto+Condensed:wght@400;700&family=Open+Sans:wght@400&display=swap">
<style>
  :root {
    --page-bg: #e9e4dc;
    --paper: #ffffff;
    --orange: #f7a533;
    --purple: #8b3a96;
    --ink: #111111;
    --white: #ffffff;
    --shade: rgba(30, 26, 24, 0.72);
  }
  html, body {
    margin: 0;
    padding: 0;
    width: 1200px;
    height: 1200px;
    overflow: hidden;
    background: var(--page-bg);
  }
  .flyer {
    position: absolute;
    left: 202px;
    top: 35px;
    width: 788px;
    height: 1107px;
    background: var(--paper);
    overflow: hidden;
    box-shadow: 0 2px 10px rgba(0,0,0,0.25);
  }
  .hero-photo {
    position: absolute;
    left: 0; top: 0;
    width: 788px;
    height: 1058px;
    background:
      linear-gradient(180deg, #ffffff 0%, #ffffff 15%, rgba(255,255,255,0) 30%),
      radial-gradient(ellipse 140px 260px at 190px 560px, #b7c884 0%, rgba(183,200,132,0) 100%),
      radial-gradient(ellipse 170px 330px at 400px 620px, #e58c98 0%, rgba(229,140,152,0) 100%),
      radial-gradient(ellipse 140px 260px at 640px 560px, #9f7cb6 0%, rgba(159,124,182,0) 100%),
      linear-gradient(180deg, #9b9591 0%, #6f6660 60%, #4a3f3a 100%);
  }
  .brand {
    position: absolute;
    top: 125px;
    left: 0;
    width: 788px;
    display: flex;
    justify-content: center;
    align-items: center;
    gap: 14px;
  }
  .brand-dot {
    width: 44px; height: 44px;
    border-radius: 50%;
    background: var(--orange);
  }
  .brand-name {
    font-family: "Roboto Condensed", sans-serif;
    font-weight: 700;
    font-size: 46px;
    color: var(--purple);
    letter-spacing: 1px;
    line-height: 1;
  }
  .headline-natural {
    position: absolute;
    z-index: 2;
    top: 543px;
    left: 0;
    width: 788px;
    margin: 0;
    text-align: center;
    font-family: "Archivo Black", sans-serif;
    font-weight: 400;
    font-size: 134px;
    line-height: 1;
    color: var(--white);
    text-shadow: -5px 4px 0 var(--ink);
    letter-spacing: -2px;
  }
  .band-orange {
    position: absolute;
    z-index: 1;
    top: 671px;
    left: 0;
    width: 788px;
    height: 110px;
    background: var(--orange);
    display: flex;
    justify-content: center;
    align-items: center;
    gap: 24px;
    overflow: hidden;
  }
  .band-dot {
    width: 40px; height: 40px;
    border-radius: 50%;
    background: var(--purple);
  }
  .headline-press {
    font-family: "Roboto Condensed", sans-serif;
    font-weight: 400;
    font-size: 124px;
    line-height: 1;
    color: var(--purple);
    text-shadow: -4px 3px 0 var(--ink);
    letter-spacing: -1px;
    margin-top: 6px;
  }
  .band-purple {
    position: absolute;
    top: 797px;
    left: 0;
    width: 788px;
    height: 66px;
    background: var(--purple);
    display: flex;
    justify-content: center;
    align-items: center;
  }
  .tagline {
    font-family: "Roboto Condensed", sans-serif;
    font-weight: 700;
    font-size: 52px;
    line-height: 1;
    color: var(--white);
    letter-spacing: 1px;
  }
  .message {
    position: absolute;
    top: 979px;
    left: 0;
    width: 788px;
    height: 79px;
    background: var(--shade);
    box-sizing: border-box;
    padding: 6px 25px 0 23px;
  }
  .message p {
    margin: 0;
    font-family: "Open Sans", sans-serif;
    font-size: 14.2px;
    line-height: 18.5px;
    color: var(--white);
    text-align: justify;
  }
  .footer {
    position: absolute;
    top: 1058px;
    left: 0;
    width: 788px;
    height: 49px;
    background: var(--paper);
    display: flex;
    align-items: center;
    box-sizing: border-box;
    padding: 0 24px;
    font-family: "Open Sans", sans-serif;
    font-size: 14.5px;
    color: var(--ink);
  }
  .social {
    display: flex;
    align-items: center;
    gap: 8px;
    margin-left: 16px;
  }
  .social + .social { margin-left: 28px; }
  .social-dot {
    width: 18px; height: 18px;
    border-radius: 50%;
    background: var(--purple);
  }
  .location {
    margin-left: auto;
    display: flex;
    align-items: center;
    gap: 8px;
    font-size: 12.5px;
    line-height: 16px;
  }
</style>
</head>
<body>
  <main class="flyer">
    <div class="hero-photo" role="img" aria-label="Photo of green, pink and purple smoothies in tall glasses with white straws on a rustic wooden table, with kiwi, strawberries, blueberries and mint in front"></div>

    <header class="brand">
      <span class="brand-dot"></span>
      <span class="brand-name">TWIRL JUICE HOUSE</span>
    </header>

    <div class="band-orange">
      <span class="band-dot"></span>
      <span class="headline-press">Cold Press</span>
      <span class="band-dot"></span>
    </div>

    <h1 class="headline-natural">Natural</h1>

    <div class="band-purple">
      <span class="tagline">JUICES &amp; DELICIOUS SMOOTHIES</span>
    </div>

    <section class="message">
      <p>Thankyou for supporting your local business as we aim to provide you with a comfortable and inviting place coupled with great products that is conducive to changing people’s lives and creating a positive community through our offerings of natural cold press juices and delicious smooties!</p>
    </section>

    <footer class="footer">
      <span>Connect with</span>
      <span class="social"><span class="social-dot"></span>TWIRL _ JUICE_ HOUSE</span>
      <span class="social"><span class="social-dot"></span>twirl juice house</span>
      <span class="location">
        <svg width="20" height="24" viewBox="0 0 20 24" aria-hidden="true">
          <path d="M10 0C4.5 0 0.5 4 0.5 9.3 0.5 16 10 24 10 24s9.5-8 9.5-14.7C19.5 4 15.5 0 10 0z" fill="#111"/>
          <circle cx="10" cy="9.2" r="3.6" fill="#fff"/>
        </svg>
        <span>418 Orchard Lane<br>Millbrook, MD 20999</span>
      </span>
    </footer>
  </main>
</body>
</html>
```